For Tolva: Business cards, letterhead, envelopes and double sided page

For Tolva: Previously described in email.

Business cards, letterhead, envelopes, and glossy marketing double sided page.

Marketing

```html
<!DOCTYPE html>
<html lang="en">
<head>
<meta charset="utf-8">
<title>Tolva Letterhead</title>
<link href="https://fonts.googleapis.com/css2?family=Arimo:wght@400;700&display=swap" rel="stylesheet">
<style>
  :root {
    --ink: #2c3048;
    --band-start: #2b3049;
    --band-end: #454f58;
    --paper: #ffffff;
  }
  * { margin: 0; padding: 0; box-sizing: border-box; }
  html, body { width: 849px; height: 1200px; overflow: hidden; background: var(--paper); }
  .letterhead {
    position: relative;
    width: 849px;
    height: 1200px;
    background: var(--paper);
    font-family: "Arimo", Arial, sans-serif;
  }
  .brand {
    position: absolute;
    top: 31px;
    left: 245px;
    display: flex;
    align-items: center;
    gap: 20px;
  }
  .brand-mark {
    width: 132px;
    height: 92px;
    border-radius: 12px;
    background: var(--ink);
  }
  .brand-name {
    font-size: 94px;
    font-weight: 700;
    color: var(--ink);
    letter-spacing: -2px;
    line-height: 1;
  }
  .brand-web {
    position: absolute;
    top: 133px;
    right: 229px;
    font-size: 21px;
    letter-spacing: 1.5px;
    color: var(--ink);
  }
  .footer-band {
    position: absolute;
    left: 0;
    bottom: 0;
    width: 849px;
    height: 144px;
  }
  .footer-contact {
    position: absolute;
    left: 325px;
    top: 1069px;
    list-style: none;
    color: var(--paper);
    font-weight: 700;
    font-size: 16px;
    line-height: 25px;
  }
</style>
</head>
<body>
  <main class="letterhead">
    <header>
      <div class="brand">
        <span class="brand-mark" aria-hidden="true"></span>
        <span class="brand-name">Tolva</span>
      </div>
      <p class="brand-web">www.tolvaline.com</p>
    </header>

    <footer>
      <svg class="footer-band" viewBox="0 0 849 144" aria-hidden="true">
        <defs>
          <linearGradient id="bandFill" x1="0" y1="0" x2="1" y2="0">
            <stop offset="0" stop-color="var(--band-start)"/>
            <stop offset="0.6" stop-color="var(--band-start)"/>
            <stop offset="1" stop-color="var(--band-end)"/>
          </linearGradient>
        </defs>
        <path d="M0 20 Q0 0 20 0 H829 Q849 0 849 20 V144 H0 Z" fill="url(#bandFill)"/>
        <path d="M2 14 Q50 118 322 144 L306 144 Q40 124 0 28 Z" fill="var(--paper)"/>
        <path d="M500 144 Q790 136 849 22 L849 34 Q790 142 520 144 Z" fill="var(--paper)"/>
      </svg>
      <ul class="footer-contact">
        <li>Address</li>
        <li>phone</li>
        <li>email</li>
        <li>website</li>
      </ul>
    </footer>
  </main>
</body>
</html>
```